Regional health service needs a PowerPoint design

We are a new organisation responsible for the purchasing of health services for the population of Basildon and Brentwood in Essex, UK - a population of c.300,000.

We are looking for a set of powerpoint master slides for use principally as 'talk books' and reports for presenting information regarding the performance of the organisation externally and to use as the basis for producing internal reports and communications.

We would like to see designs which portray the organisation as being new and different from historic PCR organisations, whilst following the principles outlined within National PCR brand guidelines (see attached). The slides should communicate creativity and professionalism.

Our logo is available on request (due to technical issues, we cannot upload onto here).

Our brand guidelines are available at:
http://www.carebrandhub.example.org/all-guidelines/guidelines/approved-care-purchasing-bodies/introduction

An example report (which we would look to move over to our new template) is available at:
http://www.marlowfieldandcresthamcpg.example.org/key-documents/doc_download/142-integrated-plan-2013-15

Further information on us is available on our website: www.marlowfieldandcresthamcpg.example.org

Target audience is healthcare professionals and the general public.

Health

• Include the organisations logo and provide a cover sheet front page and 3/4 slides showing how reports could be structured (e.g. narrative and graphical information / tabular information / use of photos etc).

Typefaces and colour schemes should be in line with our brand guidelines (i.e. principal use of Arial). Our guidelines are available at:

• As an organisation we are made up of four localities, it would be good to see designs that draw on this element of our organisation.

```html
<!DOCTYPE html>
<html lang="en">
<head>
<meta charset="utf-8">
<title>Table of Contents – Integrated Plan 2013-2015</title>
<link rel="stylesheet" href="https://fonts.googleapis.com/css2?family=Open+Sans:wght@300;400;700&display=swap">
<style>
  :root {
    --backdrop: #444444;
    --paper: #ffffff;
    --brand-blue: #1a6fb5;
    --rule-blue: #1b7ac4;
    --ink: #3f3f3f;
    --ink-dark: #1e1e1e;
    --green: #8cb319;
    --blue: #0a86c9;
    --magenta: #b5076b;
    --orange: #f39c0b;
    --footer-band: #e4e2ef;
  }
  * { margin: 0; padding: 0; box-sizing: border-box; }
  html, body {
    width: 1200px; height: 912px; overflow: hidden;
    background: var(--backdrop);
    font-family: "Open Sans", Arial, sans-serif;
  }
  .slide {
    position: absolute; left: 24px; top: 22px;
    width: 1152px; height: 866px;
    background: var(--paper);
    border-top: 4px solid var(--rule-blue);
    overflow: hidden;
  }
  .slide-header {
    position: absolute; left: 0; top: 0; width: 100%; height: 106px;
    background: var(--paper);
    box-shadow: 0 4px 8px rgba(0,0,0,0.08);
  }
  .slide-title {
    position: absolute; left: 26px; top: 26px;
    font-size: 42px; font-weight: 400; letter-spacing: 0.5px;
    color: var(--brand-blue);
  }
  .org-mark {
    position: absolute; right: 14px; top: 16px;
    display: flex; align-items: flex-start; gap: 10px;
  }
  .org-square {
    width: 20px; height: 20px; margin-top: 4px;
    background: var(--brand-blue);
  }
  .org-name {
    text-align: right; font-size: 18px; line-height: 23px;
    font-weight: 700; color: var(--ink-dark);
  }
  .contents {
    list-style: none;
  }
  .contents-item {
    position: absolute; display: flex; align-items: center;
    height: 82px;
  }
  .item-number {
    flex: none; width: 82px; height: 82px;
    display: flex; align-items: center; justify-content: center;
    color: #fff; font-size: 46px; font-weight: 300;
  }
  .item-label {
    margin-left: 20px; font-size: 25px; line-height: 35px;
    font-weight: 300; color: var(--ink);
  }
  .is-green { background: var(--green); }
  .is-blue { background: var(--blue); }
  .is-magenta { background: var(--magenta); }
  .is-orange { background: var(--orange); }
  .col-left { left: 86px; }
  .col-right { left: 604px; }
  .row-1 { top: 208px; }
  .row-2 { top: 317px; }
  .row-3 { top: 425px; }
  .row-4 { top: 534px; }
  .row-5 { top: 643px; }
  .slide-footer {
    position: absolute; left: 0; top: 822px; width: 100%; height: 38px;
    background: var(--footer-band);
    font-size: 16px; color: var(--ink);
  }
  .footer-text { position: absolute; top: 8px; }
  .footer-plan { left: 16px; }
  .footer-conf { left: 388px; }
  .footer-copy { left: 670px; }
  .footer-page { left: 948px; }
  .colour-strip {
    position: absolute; left: 0; bottom: 0; width: 100%; height: 6px;
    display: flex;
  }
  .colour-strip span { flex: 1; }
</style>
</head>
<body>
<main class="slide">
  <header class="slide-header">
    <h1 class="slide-title">TABLE OF CONTENTS</h1>
    <div class="org-mark">
      <div class="org-name">Marlowfield and Crestham<br>Care Purchasing Group</div>
      <div class="org-square"></div>
    </div>
  </header>

  <ol class="contents">
    <li class="contents-item col-left row-1"><span class="item-number is-green">01</span><span class="item-label">Introduction to Marlowfield and<br>Crestham CPG</span></li>
    <li class="contents-item col-right row-1"><span class="item-number is-green">02</span><span class="item-label">The Health of our population</span></li>
    <li class="contents-item col-left row-2"><span class="item-number is-blue">03</span><span class="item-label">Our Strategy 2013-15</span></li>
    <li class="contents-item col-right row-2"><span class="item-number is-blue">04</span><span class="item-label">Challenges in our Local System</span></li>
    <li class="contents-item col-left row-3"><span class="item-number is-magenta">05</span><span class="item-label">Work Programmes to Deliver<br>the Strategy</span></li>
    <li class="contents-item col-right row-3"><span class="item-number is-magenta">06</span><span class="item-label">Finance Strategy and Our<br>Commissioning Intentions</span></li>
    <li class="contents-item col-left row-4"><span class="item-number is-orange">07</span><span class="item-label">Annual Operating plan<br>2013/14</span></li>
    <li class="contents-item col-right row-4"><span class="item-number is-orange">08</span><span class="item-label">Risk Management &amp; Monitoring of<br>Integrated Strategy</span></li>
    <li class="contents-item col-left row-5"><span class="item-number is-green">09</span><span class="item-label">Commissining Intentions 2013/14<br>Collaborative Arrangements</span></li>
    <li class="contents-item col-right row-5"><span class="item-number is-green">10</span><span class="item-label">Appendices : How we are delivering<br>national requirements</span></li>
  </ol>

  <footer class="slide-footer">
    <span class="footer-text footer-plan">Integrated Plan 2013-2015</span>
    <span class="footer-text footer-conf">Confidential</span>
    <span class="footer-text footer-copy">Copyright 2013</span>
    <span class="footer-text footer-page">Slide 01 / 10</span>
  </footer>
  <div class="colour-strip">
    <span class="is-green"></span><span class="is-blue"></span><span class="is-orange"></span><span class="is-magenta"></span>
  </div>
</main>
</body>
</html>
```